Whitening Flyer

I need an informational flyer for my dental practice. The flyer will describe the whitening services that are available at my practice and show price of each whitening service. We currently gave a 3 fold brochure, but I prefer something with a more professional look, and personalized with our branding and practice colors. I have attached the current flyer for you to use similar text. I will also attach a flyer that I have used in the past that could demonstrate my branding or feel free to view my website: www.pemtrix.com

```html
<!DOCTYPE html>
<html lang="en">
<head>
<meta charset="utf-8">
<title>Whitening Brochure – Brightline Dental Studio</title>
<link href="https://fonts.googleapis.com/css2?family=Kanit:wght@600;700&family=Ubuntu:wght@400;500;700&display=swap" rel="stylesheet">
<style>
  :root{
    --crimson:#d3143f;
    --crimson-dark:#b80f35;
    --crimson-soft:#e8546f;
    --gold:#ffd23f;
    --ink:#2a2a2a;
    --paper:#ffffff;
    --backdrop:#e9e9ea;
    --photo-light:#e9d6cf;
    --photo-mid:#b98a74;
    --photo-dark:#5a3a2e;
    --map-tone:#e7ece9;
  }
  *{box-sizing:border-box;margin:0;padding:0}
  html,body{width:1200px;height:903px;overflow:hidden;background:var(--backdrop)}
  body{font-family:"Ubuntu",sans-serif;color:var(--ink)}
  .brochure{position:absolute;left:15px;top:0;width:1170px;height:903px;display:flex}
  .panel{position:relative;width:390px;height:903px;overflow:hidden}
  .panel--left{background:linear-gradient(90deg,#fff 80%,#f0f0f0)}
  .panel--middle{background:var(--crimson);color:#fff;text-align:center}
  .panel--cover{background:linear-gradient(90deg,#efefef,#fff 18%)}

  /* left panel */
  .section-title{position:absolute;left:35px;top:30px;font-family:"Kanit",sans-serif;font-weight:700;font-size:23px;color:var(--crimson);letter-spacing:.2px}
  .intro{position:absolute;left:35px;top:66px;width:320px;font-size:13px;line-height:17.6px;text-align:justify}
  .steps{position:absolute;left:35px;top:160px;width:320px}
  .steps__line{position:absolute;left:21px;top:20px;width:2px;height:310px;background:var(--gold)}
  .step{position:absolute;left:0;display:flex;gap:15px;width:320px}
  .step__num{flex:none;width:42px;height:42px;border-radius:50%;border:3px solid var(--gold);background:var(--crimson);color:#fff;font-family:"Kanit",sans-serif;font-size:22px;line-height:36px;text-align:center;box-shadow:0 0 0 2px #fff inset}
  .step__text{font-size:13px;line-height:17.6px;text-align:justify;padding-top:-2px}
  .step__text b{font-weight:500}
  .family-photo{position:absolute;left:0;bottom:0}

  /* middle panel */
  .office-title{margin-top:36px;font-family:"Kanit",sans-serif;font-weight:600;font-size:20px;color:var(--gold)}
  .office-text{margin:6px auto 0;width:330px;font-size:12.5px;line-height:17.6px}
  .map{position:absolute;left:83px;top:155px;width:236px;height:236px;border-radius:50%;border:12px solid var(--crimson-soft);background:var(--map-tone);box-shadow:0 8px 14px rgba(0,0,0,.18)}
  .brand-name{font-weight:500;white-space:nowrap}
  .brand-name--mid{position:absolute;left:0;right:0;top:440px;font-size:24px;color:#fff}
  .contact-title{position:absolute;left:0;right:0;top:545px;font-family:"Kanit",sans-serif;font-weight:600;font-size:17px;color:var(--gold)}
  .contact-list{position:absolute;left:0;right:0;top:580px;list-style:none;font-size:13px;line-height:17.6px}
  .contact-list li{display:flex;flex-direction:column;align-items:center;margin-bottom:14px}
  .contact-list svg{margin-bottom:5px}
  .follow{position:absolute;left:0;right:0;top:820px;font-size:13px;line-height:17px}
  .follow__title{font-family:"Kanit",sans-serif;font-weight:600;font-size:17px;color:var(--gold);margin-bottom:2px}
  .follow b{font-weight:700}

  /* cover panel */
  .brand-name--cover{position:absolute;left:0;right:0;top:75px;text-align:center;font-size:34px;color:var(--crimson)}
  .cover-kicker{position:absolute;left:0;right:0;top:240px;text-align:center;font-size:19px;font-weight:500;letter-spacing:.4px}
  .cover-title{position:absolute;left:0;right:0;top:278px;text-align:center;font-family:"Kanit",sans-serif;font-weight:700;font-size:38px;line-height:43px;color:var(--crimson)}
  .cover-doctor{position:absolute;left:0;right:0;top:380px;text-align:center;font-size:18px;font-weight:500}
  .cover-photo{position:absolute;left:0;top:440px}
  .cover-url{position:absolute;left:0;right:0;bottom:20px;text-align:center;font-size:16px;font-weight:500;color:#222}
</style>
</head>
<body>
<main class="brochure">

  <section class="panel panel--left">
    <h2 class="section-title">HOW DO YOU GET STARTED?</h2>
    <p class="intro">There are many options and factors to take into account when deciding which whitening option is best for you. Our team is here to help you in the decision process. Some deciding factors include;</p>
    <div class="steps">
      <span class="steps__line"></span>
      <div class="step" style="top:0">
        <span class="step__num">1</span>
        <p class="step__text"><b>The Cost:</b> cost can range anywhere from $30 for over the counter treatment to $600 for some in office treatments</p>
      </div>
      <div class="step" style="top:90px">
        <span class="step__num">2</span>
        <p class="step__text"><b>The Effort:</b> In office treatment can take as little time as 1 ½ hours whereas over the counter treatment can take up to 3 weeks to see a difference.</p>
      </div>
      <div class="step" style="top:195px">
        <span class="step__num">3</span>
        <p class="step__text"><b>The Sensitivity:</b> If you suffer from sensitive gums or teeth some of the stronger treatments may not be the best option for you.</p>
      </div>
      <div class="step" style="top:305px">
        <span class="step__num">4</span>
        <p class="step__text"><b>The RESULTS:</b> There is a significant difference in the active whitening ingredient that is allowed in OTC products vs. In Office solution will make your teeth brighter, faster.</p>
      </div>
    </div>
    <svg class="family-photo" width="390" height="300" viewBox="0 0 390 300">
      <defs>
        <linearGradient id="familyTone" x1="0" y1="0" x2="1" y2="1">
          <stop offset="0" stop-color="#f1e2d8"/>
          <stop offset=".6" stop-color="#caa996"/>
          <stop offset="1" stop-color="#9e9e9e"/>
        </linearGradient>
      </defs>
      <path d="M0 40 C40 10 90 40 140 50 C200 60 230 20 280 10 C330 0 370 60 390 120 L390 300 L0 300Z" fill="var(--crimson)"/>
      <path role="img" aria-label="Photo of a smiling family of four" d="M0 70 C50 45 110 70 170 70 C220 70 250 30 290 25 C340 20 370 80 375 140 L370 300 L0 300Z" fill="url(#familyTone)"/>
    </svg>
  </section>

  <section class="panel panel--middle">
    <h3 class="office-title">Office Information</h3>
    <p class="office-text">our office is conveniently located on Harbor Avenue, one block east of the Westfield Parkway, and easily accessible via the Harbor streetcar.</p>
    <div class="map" role="img" aria-label="Street map showing the office location"></div>
    <p class="brand-name brand-name--mid">Brightline Dental Studio</p>
    <h3 class="contact-title">CONTACT US</h3>
    <ul class="contact-list">
      <li>
        <svg width="22" height="22" viewBox="0 0 22 22"><circle cx="11" cy="11" r="11" fill="var(--gold)"/><path d="M11 5a4 4 0 0 0-4 4c0 3 4 7 4 7s4-4 4-7a4 4 0 0 0-4-4z" fill="var(--crimson)"/><circle cx="11" cy="9" r="1.5" fill="var(--gold)"/></svg>
        <span>1840 Harbor Ave, Riverton,<br>LA 70455</span>
      </li>
      <li>
        <svg width="22" height="22" viewBox="0 0 22 22"><circle cx="11" cy="11" r="11" fill="var(--gold)"/><path d="M7 6l2.5-.5 1.3 3-1.5 1a7 7 0 0 0 3.2 3.2l1-1.5 3 1.3-.5 2.5C12 16 6 10 7 6z" fill="var(--crimson)"/></svg>
        <span>555-204-7718</span>
      </li>
      <li>
        <svg width="22" height="22" viewBox="0 0 22 22"><circle cx="11" cy="11" r="11" fill="var(--gold)"/><rect x="5.5" y="7" width="11" height="8" rx="1" fill="var(--crimson)"/><path d="M5.5 7.5l5.5 4 5.5-4" stroke="var(--gold)" stroke-width="1.2" fill="none"/></svg>
        <span>info@pemtrix.com</span>
      </li>
      <li>
        <svg width="22" height="22" viewBox="0 0 22 22"><circle cx="11" cy="11" r="11" fill="var(--gold)"/><g stroke="var(--crimson)" stroke-width="1.3" fill="none"><circle cx="11" cy="11" r="6"/><ellipse cx="11" cy="11" rx="2.6" ry="6"/><path d="M5 11h12"/></g></svg>
        <span>www.pemtrix.com</span>
      </li>
    </ul>
    <div class="follow">
      <p class="follow__title">Follow Us:</p>
      <p><b>Instagram:</b> brightline_dental_studio</p>
      <p><b>Facebook:</b> Brightline Dental Studio</p>
    </div>
  </section>

  <section class="panel panel--cover">
    <p class="brand-name brand-name--cover">Brightline Dental Studio</p>
    <p class="cover-kicker">BRIGHTLINE DENTAL STUDIO</p>
    <h1 class="cover-title">WHICH WHITENING<br>IS RIGHT?</h1>
    <p class="cover-doctor">Dr. Lena Moreau DMD</p>
    <svg class="cover-photo" width="390" height="463" viewBox="0 0 390 463">
      <defs>
        <linearGradient id="groupTone" x1="0" y1="0" x2="0" y2="1">
          <stop offset="0" stop-color="var(--photo-dark)"/>
          <stop offset=".45" stop-color="var(--photo-mid)"/>
          <stop offset=".8" stop-color="#f4f0ee"/>
          <stop offset="1" stop-color="#ffffff"/>
        </linearGradient>
      </defs>
      <path d="M0 463 L0 150 C0 60 50 10 110 8 C160 6 200 60 260 55 C320 50 360 10 390 0 L390 463Z" fill="var(--crimson)"/>
      <path d="M45 463 C20 400 10 300 30 200 C55 90 110 50 170 55 C230 60 300 70 390 40 L390 463Z" fill="#fff"/>
      <path role="img" aria-label="Photo of three smiling friends in white shirts" d="M48 463 C25 400 18 300 38 205 C62 100 115 62 172 66 C235 70 300 80 390 52 L390 420 L48 463Z" fill="url(#groupTone)"/>
    </svg>
    <p class="cover-url">www.pemtrix.com</p>
  </section>

</main>
</body>
</html>
```